MORVANE GROUP (STATIONARY)
MORVANE CONSULTING GROUP, LLC
Please update design to show my name next to the Title, Principal : Delbert T. Worrow III
Also, please fix the address in the design :
4827 Halvorsen St. NW, Washington, DC 20374
Last, I am also looking for other stationary such as letterhead , letters and invoices. (not just the business card)
Thank you!
Delbert

```html
<!DOCTYPE html>
<html lang="en">
<head>
<meta charset="utf-8">
<title>Morvane Group Stationery</title>
<link href="https://fonts.googleapis.com/css2?family=Montserrat:wght@500;600&family=Open+Sans:wght@400;600&display=swap" rel="stylesheet">
<style>
  :root {
    --backdrop: #e9e4dc;
    --paper: #ffffff;
    --orange: #f7941d;
    --green: #8dc63f;
    --ink: #3b3b3b;
    --muted: #8a8a8a;
  }
  * { box-sizing: border-box; margin: 0; padding: 0; }
  html, body { width: 1200px; height: 562px; overflow: hidden; }
  body {
    position: relative;
    background: var(--backdrop);
    font-family: "Open Sans", Arial, sans-serif;
    color: var(--ink);
  }
  .piece-label {
    position: absolute;
    font-size: 8px;
    font-weight: 600;
    color: var(--ink);
    text-align: center;
  }
  .sheet {
    position: absolute;
    background: var(--paper);
    box-shadow: 0 2px 6px rgba(0,0,0,.25);
    overflow: hidden;
  }
  .sheet svg.accent { position: absolute; inset: 0; width: 100%; height: 100%; }
  .brand {
    position: absolute;
    display: flex;
    align-items: center;
    gap: 6px;
    font-family: "Montserrat", Arial, sans-serif;
    font-weight: 600;
    color: var(--ink);
    letter-spacing: .04em;
    white-space: nowrap;
  }
  .brand .dot { border-radius: 50%; background: var(--orange); flex: none; }
  .brand-sm { font-size: 11px; }
  .brand-sm .dot { width: 14px; height: 14px; }
  .brand-xs { font-size: 7px; gap: 4px; line-height: 1.15; }
  .brand-xs .dot { width: 10px; height: 10px; }
  .footer-line {
    position: absolute;
    left: 48px; right: 10px; bottom: 10px;
    font-size: 5px;
    color: var(--muted);
    white-space: nowrap;
    text-align: center;
  }

  /* Fax cover */
  .fax { left: 36px; top: 19px; width: 348px; height: 511px; }
  .fax .fax-title {
    position: absolute; right: 22px; top: 60px;
    font-family: "Montserrat", Arial, sans-serif; font-size: 10px; font-weight: 600;
  }
  .fax-form {
    position: absolute; left: 22px; top: 78px; width: 304px;
    border: 1px solid var(--ink); border-collapse: collapse;
    font-size: 7px;
  }
  .fax-form td { border: 1px solid var(--ink); height: 18px; padding: 2px 4px; width: 50%; vertical-align: top; }
  .fax-options {
    position: absolute; left: 22px; top: 180px; width: 304px;
    display: flex; justify-content: space-between; font-size: 6.5px;
  }
  .fax-options span::before {
    content: ""; display: inline-block; width: 6px; height: 6px;
    border: 1px solid var(--ink); margin-right: 3px; vertical-align: -1px;
  }

  /* Letterhead */
  .letterhead { left: 408px; top: 19px; width: 355px; height: 511px; }

  /* Business cards */
  .card { width: 161px; height: 91px; top: 29px; }
  .card-front { left: 780px; }
  .card-back { left: 963px; background: var(--orange); }
  .card-details {
    position: absolute; left: 84px; top: 24px;
    font-size: 4.4px; line-height: 1.45; color: var(--ink);
    white-space: nowrap;
  }
  .card-details strong { font-size: 5.2px; font-weight: 600; display: block; }
  .card-back .mark {
    position: absolute; left: 63px; top: 28px; width: 34px; height: 34px;
    border-radius: 50%; background: var(--paper);
  }

  /* Envelopes */
  .envelope-front { left: 780px; top: 145px; width: 348px; height: 240px; }
  .envelope-front .return-address {
    position: absolute; left: 22px; top: 88px; font-size: 5.5px; color: var(--muted);
  }
  .envelope-back { left: 780px; top: 400px; width: 348px; height: 152px; }
  .envelope-back .mark {
    position: absolute; left: 162px; top: 14px; width: 24px; height: 24px;
    border-radius: 50%; background: var(--paper);
  }
</style>
</head>
<body>

  <div class="piece-label" style="left:36px;top:5px;width:348px;">Fax Cover</div>
  <div class="piece-label" style="left:408px;top:5px;width:355px;">Letterhead</div>
  <div class="piece-label" style="left:780px;top:15px;width:161px;">Business Card (Front)</div>
  <div class="piece-label" style="left:963px;top:15px;width:161px;">Business Card (Back)</div>
  <div class="piece-label" style="left:780px;top:131px;width:348px;">Envelope (Front)</div>
  <div class="piece-label" style="left:780px;top:388px;width:348px;">Envelope (Back)</div>

  <!-- Fax cover -->
  <section class="sheet fax">
    <svg class="accent" viewBox="0 0 348 511" preserveAspectRatio="none" aria-hidden="true">
      <path d="M250 0 Q330 8 348 70 L348 0 Z" fill="var(--orange)"/>
      <path d="M240 0 Q326 10 348 80" fill="none" stroke="var(--green)" stroke-width="1.5"/>
      <path d="M0 462 Q8 506 38 511 L0 511 Z" fill="var(--orange)"/>
      <path d="M0 454 Q10 509 46 511" fill="none" stroke="var(--green)" stroke-width="1.5"/>
    </svg>
    <div class="brand brand-sm" style="left:22px;top:44px;"><span class="dot"></span>MORVANE GROUP</div>
    <div class="fax-title">FAX</div>
    <table class="fax-form">
      <tr><td>To:</td><td>From:</td></tr>
      <tr><td>Fax:</td><td>Pages:</td></tr>
      <tr><td>Phone:</td><td>Date:</td></tr>
      <tr><td>Re:</td><td>CC:</td></tr>
    </table>
    <div class="fax-options">
      <span>Urgent</span><span>For Review</span><span>Please Comment</span><span>Please Reply</span><span>Please Recycle</span>
    </div>
    <div class="footer-line">4827 Halvorsen St. NW, Washington, DC 20374 &nbsp;|&nbsp; (202) 555-0164 &nbsp;|&nbsp; morvaneconsulting@mailbox.net</div>
  </section>

  <!-- Letterhead -->
  <section class="sheet letterhead">
    <svg class="accent" viewBox="0 0 355 511" preserveAspectRatio="none" aria-hidden="true">
      <path d="M260 0 Q338 8 355 70 L355 0 Z" fill="var(--orange)"/>
      <path d="M250 0 Q334 10 355 80" fill="none" stroke="var(--green)" stroke-width="1.5"/>
      <path d="M0 462 Q8 506 38 511 L0 511 Z" fill="var(--orange)"/>
      <path d="M0 454 Q10 509 46 511" fill="none" stroke="var(--green)" stroke-width="1.5"/>
    </svg>
    <div class="brand brand-sm" style="left:128px;top:44px;"><span class="dot"></span>MORVANE GROUP</div>
    <div class="footer-line">4827 Halvorsen St. NW, Washington, DC 20374 &nbsp;|&nbsp; (202) 555-0164 &nbsp;|&nbsp; morvaneconsulting@mailbox.net</div>
  </section>

  <!-- Business card front -->
  <section class="sheet card card-front">
    <svg class="accent" viewBox="0 0 161 91" preserveAspectRatio="none" aria-hidden="true">
      <path d="M0 72 Q8 89 40 91 L0 91 Z" fill="var(--orange)"/>
      <path d="M0 66 Q8 90 46 91" fill="none" stroke="var(--green)" stroke-width="1"/>
    </svg>
    <div class="brand brand-xs" style="left:12px;top:34px;"><span class="dot"></span><span>MORVANE<br>GROUP</span></div>
    <div class="card-details">
      <strong>Delbert T. Worrow III</strong>
      Principal<br>
      4827 Halvorsen St. NW<br>
      Washington, DC 20374<br>
      (202) 555-0164<br>
      morvaneconsulting@mailbox.net
    </div>
  </section>

  <!-- Business card back -->
  <section class="sheet card card-back">
    <div class="mark" role="img" aria-label="Morvane Group mark"></div>
  </section>

  <!-- Envelope front -->
  <section class="sheet envelope-front">
    <svg class="accent" viewBox="0 0 348 240" preserveAspectRatio="none" aria-hidden="true">
      <path d="M250 0 Q330 6 348 50 L348 0 Z" fill="var(--orange)"/>
      <path d="M240 0 Q326 8 348 58" fill="none" stroke="var(--green)" stroke-width="1.5"/>
      <path d="M0 190 Q20 236 110 240 L0 240 Z" fill="var(--orange)"/>
      <path d="M0 182 Q22 239 122 240" fill="none" stroke="var(--green)" stroke-width="1.5"/>
    </svg>
    <div class="brand brand-sm" style="left:22px;top:66px;"><span class="dot"></span>MORVANE GROUP</div>
    <div class="return-address">4827 Halvorsen St. NW, Washington, DC 20374</div>
  </section>

  <!-- Envelope back -->
  <section class="sheet envelope-back">
    <svg class="accent" viewBox="0 0 348 152" preserveAspectRatio="none" aria-hidden="true">
      <path d="M0 0 L348 0 L348 30 L174 58 L0 30 Z" fill="var(--orange)"/>
    </svg>
    <div class="mark" role="img" aria-label="Morvane Group mark"></div>
  </section>

</body>
</html>
```